Stationery for a professional investment company

Hi, I would like to design full stationary set based on my logo. I would like to use the red color in the file as well as white.

The design should be simple, credible and serious.

Q7 manages portfolio companies. The companies that represent our industry are

LMW (https://www.lmw-example.com)

RNB Capital

Target Market(s)

Investment professionals

Industry/Entity Type

Investment Advisory

Font styles to use
Sans Serif

Colors
ec1f27

Requirements
Must have
• A4 Letterhead, C4 envelop, C5 envelop, DL envelop

```html
<!DOCTYPE html>
<html lang="en">
<head>
<meta charset="utf-8">
<title>Q7 Advisory — Stationery Set</title>
<link href="https://fonts.googleapis.com/css2?family=Arimo:wght@400;700&display=swap" rel="stylesheet">
<style>
  :root {
    --brand-red: #87222b;
    --paper: #ffffff;
    --folder-white: #f4f4f4;
    --backdrop: #dadada;
    --ink: #2b2b2b;
    --ink-soft: #555555;
  }
  * { box-sizing: border-box; margin: 0; padding: 0; }
  html, body { width: 1200px; height: 991px; overflow: hidden; }
  body {
    position: relative;
    background: var(--backdrop);
    font-family: "Arimo", Arial, sans-serif;
    color: var(--ink);
  }
  .wordmark {
    font-family: "Arimo", Arial, sans-serif;
    font-weight: 700;
    color: var(--brand-red);
    white-space: nowrap;
    line-height: 1;
  }
  .wordmark--light { color: var(--paper); }

  /* Letterhead */
  .letterhead {
    position: absolute; left: 71px; top: 104px; width: 398px; height: 560px;
    background: var(--paper);
    border-bottom: 5px solid var(--brand-red);
  }
  .letterhead .wordmark { position: absolute; left: 35px; top: 38px; font-size: 16px; }
  .letterhead__contact {
    position: absolute; left: 286px; top: 38px;
    font-size: 4.6px; line-height: 6px; color: var(--ink-soft);
  }
  .letterhead__address { border-left: 1.5px solid var(--brand-red); padding-left: 4px; margin-bottom: 5px; }
  .contact-line { display: flex; align-items: center; gap: 3px; }
  .contact-line svg { width: 5px; height: 5px; flex: none; }
  .letter {
    position: absolute; left: 35px; top: 130px; width: 328px;
    font-size: 5.4px; line-height: 7px; color: var(--ink);
  }
  .letter__recipient { margin-bottom: 28px; }
  .letter__salutation { font-weight: 700; margin-bottom: 7px; }
  .letter p { margin-bottom: 7px; text-align: justify; }
  .letter__closing { margin-top: 22px; }
  .letter__signature { display: block; width: 70px; height: 28px; margin: 4px 0 10px; background: #eef0f6; }
  .letter__signer { font-weight: 700; }

  /* Presentation folder */
  .folder {
    position: absolute; left: 507px; top: 90px; width: 432px; height: 575px;
    background: var(--brand-red);
    border-radius: 3px; overflow: hidden;
  }
  .folder__top {
    position: absolute; left: 0; top: 0; width: 100%; height: 212px;
    background: var(--folder-white);
  }
  .folder__spine {
    position: absolute; left: 26px; top: 0; width: 1px; height: 100%;
    background: rgba(0,0,0,0.08);
  }
  .folder .wordmark { position: absolute; right: 36px; top: 164px; font-size: 24px; }

  /* Business cards */
  .card { position: absolute; left: 66px; width: 170px; height: 94px; }
  .card--front { top: 696px; background: var(--paper); border-bottom: 4px solid var(--brand-red); }
  .card--back { top: 810px; background: var(--brand-red); display: flex; align-items: center; justify-content: center; }
  .card__name { position: absolute; left: 12px; top: 16px; font-size: 5.4px; font-weight: 700; color: var(--brand-red); text-transform: uppercase; }
  .card__title { position: absolute; left: 12px; top: 23px; font-size: 3.6px; color: var(--ink-soft); }
  .card--front .wordmark { position: absolute; left: 12px; top: 75px; font-size: 7.5px; }
  .card__address { position: absolute; left: 67px; top: 74px; font-size: 3.4px; line-height: 4.4px; color: var(--ink-soft); }
  .card__contact { position: absolute; left: 120px; top: 74px; font-size: 3.4px; line-height: 4.4px; color: var(--ink-soft); }
  .card__contact .contact-line svg { width: 3.4px; height: 3.4px; }
  .card--back .wordmark { font-size: 12px; }

  /* Envelopes */
  .envelope { position: absolute; top: 696px; width: 415px; height: 208px; background: var(--paper); }
  .envelope--window { left: 266px; border-bottom: 5px solid var(--brand-red); }
  .envelope--window .wordmark { position: absolute; left: 19px; top: 178px; font-size: 11px; }
  .envelope__return { position: absolute; left: 92px; top: 177px; font-size: 4.8px; line-height: 6px; color: var(--ink-soft); }
  .envelope--flap { left: 718px; }
  .envelope__flap {
    position: absolute; left: 0; top: 0; width: 100%; height: 55px;
    background: var(--brand-red);
    border-radius: 0 0 26px 26px;
    display: flex; align-items: center; justify-content: center;
  }
  .envelope__flap .wordmark { font-size: 10px; }
</style>
</head>
<body>

  <section class="letterhead" aria-label="A4 letterhead">
    <div class="wordmark">Q7 Advisory</div>
    <div class="letterhead__contact">
      <div class="letterhead__address">48 Harbor Street, Suite 1200<br>New York, New York 10011</div>
      <div class="contact-line">
        <svg viewBox="0 0 10 10"><path d="M2 1l2 2-1 1.5c.6 1.2 1.3 1.9 2.5 2.5L7 6l2 2-1.2 1.3C4.5 9 1 5.5.7 2.2z" fill="var(--brand-red)"/></svg>
        <span>+ 1 (555) 014-2200</span>
      </div>
      <div class="contact-line">
        <svg viewBox="0 0 10 10"><rect x="0.5" y="2" width="9" height="6" fill="var(--brand-red)"/><path d="M0.5 2l4.5 3.5L9.5 2" stroke="#fff" fill="none" stroke-width="0.8"/></svg>
        <span>info@lmw-example.com</span>
      </div>
      <div class="contact-line">
        <svg viewBox="0 0 10 10"><circle cx="5" cy="5" r="4.2" fill="none" stroke="var(--brand-red)" stroke-width="1"/><path d="M1 5h8M5 1c-2 2.5-2 5.5 0 8M5 1c2 2.5 2 5.5 0 8" stroke="var(--brand-red)" fill="none" stroke-width="0.7"/></svg>
        <span>www.lmw-example.com</span>
      </div>
    </div>

    <article class="letter">
      <div class="letter__recipient">
        Mr. Elliot Varga<br>President and CEO<br>NorthPeak Systems LLC.<br>210 Linden Avenue, Suite 300<br>New York, NY 10027
      </div>
      <div class="letter__salutation">Dear Mr. Varga:</div>
      <p>As Chairperson of the Corporate Conscience Campaign - Helping the Homeless in New York, I am writing this to thank you personally for your company's support in last month's fund-raising effort.</p>
      <p>As I indicated when we spoke on the phone two weeks ago, the campaign was considered a resounding success, raising a total of $1.65 million to-date, significantly exceeding our target of $1 million. Some donations are still trickling in, so we could end up close to a total of $2 million.</p>
      <p>NorthPeak was an influential leader throughout the entire three-month campaign. In fact, we couldn't have succeeded without the generous support of your company, both financially, and through your organizational and administrative assistance. Your Team Leader, Laura Benning was particularly impressive, going above and beyond what we could have expected of someone performing as a volunteer while continuing on with her day-to-day duties. Please convey my special thanks to Laura.</p>
      <p>I would also ask you to convey my sincere thanks and congratulations to all of those other people in your company who contributed in any way to the Helping the Homeless Campaign. Please tell them that the sum of their contributions resulted in a major success that they should all be proud of taking part in.</p>
      <p>I believe that the 27 companies that participated in this effort have set a new standard for social responsibility in this community, and have set a powerful example that will inspire other companies and organizations to do the same.</p>
      <p>I look forward to seeing you at the Mayor's special thank you reception next month.</p>
      <div class="letter__closing">Yours sincerely,</div>
      <span class="letter__signature" role="img" aria-label="Handwritten signature"></span>
      <div class="letter__signer">Martin Hale</div>
      <div>Fundraising Chair</div>
    </article>
  </section>

  <section class="folder" aria-label="Presentation folder">
    <div class="folder__top"></div>
    <div class="folder__spine"></div>
    <div class="wordmark">Q7 Advisory</div>
  </section>

  <section class="card card--front" aria-label="Business card front">
    <div class="card__name">Daniel Marsh</div>
    <div class="card__title">Co-Chairman</div>
    <div class="wordmark">Q7 Advisory</div>
    <div class="card__address">48 Harbor Street, Suite 1200<br>New York, New York 10011</div>
    <div class="card__contact">
      <div class="contact-line">
        <svg viewBox="0 0 10 10"><path d="M2 1l2 2-1 1.5c.6 1.2 1.3 1.9 2.5 2.5L7 6l2 2-1.2 1.3C4.5 9 1 5.5.7 2.2z" fill="var(--brand-red)"/></svg>
        <span>+ 1 (555) 014-2200</span>
      </div>
      <div class="contact-line">
        <svg viewBox="0 0 10 10"><rect x="0.5" y="2" width="9" height="6" fill="var(--brand-red)"/></svg>
        <span>info@lmw-example.com</span>
      </div>
    </div>
  </section>

  <section class="card card--back" aria-label="Business card back">
    <div class="wordmark wordmark--light">Q7 Advisory</div>
  </section>

  <section class="envelope envelope--window" aria-label="DL envelope">
    <div class="wordmark">Q7 Advisory</div>
    <div class="envelope__return">48 Harbor Street, Suite 1200<br>New York, New York 10011</div>
  </section>

  <section class="envelope envelope--flap" aria-label="C5 envelope back">
    <div class="envelope__flap">
      <div class="wordmark wordmark--light">Q7 Advisory</div>
    </div>
  </section>

</body>
</html>
```